Meridale Freightworks Group - needs a website

Build a simple but professional website for Meridale Freightworks Group.
Web address is www.merfregro.com.au
We have just completed developing a brochure and the contents of the brochure would serve as the web pages.
Web design does not need to deviate far from the brochure and will not include electronic commerce etc at this stage.

Target Market(s)

Privately owned logistics businesses in Australia

Industry/Entity Type

Build

Number of Pages Required

5+ page

Requirements
Must have
• Professional, elegant, ability to upload video in the future, ability to add e-commerce in the future

```html
<!DOCTYPE html>
<html lang="en">
<head>
<meta charset="utf-8">
<title>Meridale Freightworks Group</title>
<link href="https://fonts.googleapis.com/css2?family=Open+Sans:wght@400;600;700;800&display=swap" rel="stylesheet">
<style>
:root{
  --blue:#1c5ca4;
  --blue-dark:#154a88;
  --navy:#0c2748;
  --navy-2:#0f3360;
  --cyan:#39b6ee;
  --ink:#1f2a38;
  --white:#ffffff;
  --grey:#eef0f3;
  --field:#e6e8eb;
  --black:#121212;
}
*{box-sizing:border-box;margin:0;padding:0}
html,body{width:1200px;height:3502px;overflow:hidden}
body{font-family:"Open Sans",Arial,sans-serif;color:var(--ink);background:var(--white);font-size:15px;line-height:1.45}
.section-title{font-weight:800;font-size:27px;color:var(--blue-dark);text-align:center;letter-spacing:.5px}
.lead{font-size:15.5px;text-align:center;max-width:1000px;margin:10px auto 0}
.btn-dark{display:inline-block;background:var(--black);color:var(--white);font-weight:700;font-size:14px;padding:9px 30px;border-radius:3px}

/* header */
.site-header{height:142px;display:flex;align-items:center;justify-content:space-between;padding:0 48px}
.brand{display:flex;align-items:center;gap:14px}
.brand-mark{width:34px;height:34px;background:var(--blue)}
.brand-name{font-weight:800;font-size:30px;color:var(--blue)}
.brand-sub{font-weight:700;font-size:14px;color:var(--blue);line-height:1.15;max-width:150px}
.tagline{font-weight:700;font-size:17px;color:var(--blue)}

/* nav */
.main-nav{height:44px;background:var(--navy-2);display:flex;align-items:center;justify-content:space-between;padding:0 38px;margin:0 20px}
.main-nav a{color:var(--white);text-decoration:none;font-weight:700;font-size:13.5px}

/* hero */
.hero{height:510px;margin:0 20px;position:relative;background:linear-gradient(180deg,#c9cdd2 0%,#9ea6b0 45%,#5f6b78 100%)}
.hero-caption{position:absolute;right:30px;bottom:14px;width:640px;color:var(--white);background:linear-gradient(90deg,rgba(28,92,164,0),rgba(21,74,136,.95) 12%);padding:12px 16px 12px 60px}
.hero-caption h1{font-size:19px;font-weight:800}
.hero-caption p{font-size:17px;font-weight:600;line-height:1.35}

/* solution */
.solution{padding-top:40px}
.pillars{margin:30px 20px 0}
.pillar{display:flex;height:99px;background:linear-gradient(90deg,#0c2748,#1b5aa0);border-bottom:2px solid #0a1f3a}
.pillar-label{width:307px;background:var(--navy);display:flex;align-items:center;padding-left:52px;gap:30px;color:var(--cyan);font-weight:700;font-size:17px}
.pillar-icon{width:66px;height:66px;border:3px solid var(--cyan);border-radius:4px;display:flex;align-items:center;justify-content:center}
.pillar-body{flex:1;display:flex;align-items:center;padding:0 30px 0 28px}
.pillar-body ul{color:var(--white);font-size:13.5px;list-style:none}
.pillar-body li::before{content:"• "}

/* challenges */
.challenges{padding-top:40px}
.dynamics{height:392px;margin:22px 20px 0;background:var(--blue);padding-top:14px}
.dynamics h3{text-align:center;color:var(--cyan);font-size:17px;font-weight:700}
.dyn-grid{display:grid;grid-template-columns:repeat(6,1fr);padding:0 30px;margin-top:10px}
.dyn-cell{display:flex;flex-direction:column;align-items:center;text-align:center;color:var(--white);font-weight:700;font-size:15px;height:250px}
.dyn-top,.dyn-bot{height:125px;display:flex;align-items:center;justify-content:center;width:100%}
.dyn-cell .caret{color:var(--white);font-size:18px;line-height:1}
.dynamics .btn-dark{display:block;width:160px;margin:12px auto 0;text-align:center}

/* approach */
.approach{padding-top:46px}
.phase-row{display:flex;justify-content:center;gap:12px;margin-top:24px}
.phase{width:276px;height:42px;background:var(--blue-dark);color:var(--white);font-weight:700;font-size:16px;display:flex;align-items:center;justify-content:center;border-radius:3px}

/* membership */
.membership{height:484px;margin:32px 20px 0;background:var(--blue);color:var(--white);padding-top:28px}
.membership .section-title{color:var(--white)}
.membership .lead{color:var(--white)}
.terms{display:grid;grid-template-columns:repeat(5,1fr);margin:34px 60px 0;gap:24px}
.term{text-align:center}
.term svg{height:76px}
.term h4{color:var(--cyan);font-size:16px;font-weight:700;margin-top:8px}
.term p{font-size:13px;font-weight:600;line-height:1.4}

/* objectives */
.objectives{padding-top:40px;text-align:center;height:244px}
.objectives .btn-dark{margin-top:24px}

/* team */
.team{height:408px;margin:0 20px;background:var(--blue);color:var(--white);position:relative;padding:32px 0 0 28px}
.team h2{font-size:25px;font-weight:800}
.team-bio{width:420px;font-size:13px;font-weight:600;margin-top:8px}
.team-bio ul{list-style:none}
.team-bio .ticks li::before{content:"✓ ";color:var(--cyan)}
.carousel{position:absolute;left:490px;top:75px;width:640px;height:270px}
.card{position:absolute;background:var(--white);box-shadow:0 4px 12px rgba(0,0,0,.35);display:flex;flex-direction:column;align-items:center}
.card.side{top:28px;width:170px;height:205px;background:#e9ecef}
.card.main{left:175px;width:288px;height:270px;z-index:2}
.portrait{border-radius:50%;background:linear-gradient(180deg,#c5ccd4,#7e8a98)}
.card-name{margin-top:auto;width:100%;background:#7fa9d6;color:var(--white);text-align:center;font-size:12px;padding:4px 0}
.card.main .card-name{background:var(--blue);font-size:17px;padding:8px 0;margin-bottom:26px}
.arrow{position:absolute;top:120px}

/* contact */
.contact{height:258px;display:flex;padding:28px 0 0 84px}
.contact-info{width:430px}
.contact h2{font-size:23px;font-weight:800;color:var(--blue-dark)}
.contact-line{display:flex;gap:16px;align-items:flex-start;font-size:14.5px;margin-top:12px}
.social{display:flex;gap:10px;margin:12px 0 0 40px}
.social span{width:16px;height:16px;border-radius:50%;background:var(--blue)}
.reach{flex:1;padding-right:78px}
.form{display:grid;grid-template-columns:300px 300px;column-gap:20px;row-gap:12px;margin-top:16px}
.field{height:36px;background:var(--field);font-size:13px;color:#555;padding:9px 14px}
.field.tall{grid-row:span 2;height:84px}
.send{width:100px;height:36px;background:var(--black);color:var(--white);font-weight:700;font-size:13px;display:flex;align-items:center;justify-content:center}

/* footer */
.site-footer{height:140px;background:var(--grey);display:flex;justify-content:space-between;align-items:flex-end;padding:0 48px 30px}
.copyright{font-size:11px;font-weight:700;color:var(--blue)}
</style>
</head>
<body>

<header class="site-header">
  <div class="brand">
    <span class="brand-mark"></span>
    <span class="brand-name">MFG</span>
    <span class="brand-sub">MERIDALE FREIGHTWORKS GROUP</span>
  </div>
  <div class="tagline">Scale : Synergy : Value</div>
</header>

<nav class="main-nav">
  <a>ABOUT</a><a>OUR SOLUTION</a><a>THE CHALLENGES</a><a>OUR APPROACH</a><a>KEY MEMBERSHIP TERMS</a><a>OUR OBJECTIVES</a><a>OUR TEAM</a><a>CONTACT</a>
</nav>

<section class="hero" role="img" aria-label="Warehouse interior with tall pallet racking and a forklift">
  <div class="hero-caption">
    <h1>A NEW SOLUTION FOR AUSTRALIAN WAREHOUSE BUSINESS OWNERS.</h1>
    <p>Offering national scale to increase revenues, achieving synergies to reduce costs, and enhancing the value in your business.</p>
  </div>
</section>

<section class="solution">
  <h2 class="section-title">OUR SOLUTION</h2>
  <p class="lead">Meridale Freightworks Group provides a national platform to deliver scale to its members. Through this scale, MFG and its members will secure new business. The value of members' businesses will increase, and members will be presented with multiple options to exit.</p>
  <div class="pillars">
    <div class="pillar">
      <div class="pillar-label"><span class="pillar-icon"><svg width="40" height="40" viewBox="0 0 40 40" fill="none" stroke="#39b6ee" stroke-width="3"><path d="M4 4l12 12M4 4h9M4 4v9M36 36L24 24M36 36h-9M36 36v-9M36 4L24 16M36 4h-9M36 4v9M4 36l12-12M4 36h9M4 36v-9"/></svg></span>SCALE</div>
      <div class="pillar-body"><ul><li>By leveraging its memberships and national presence, MFG will present as a premium logistics provider within the Australia market - a credible alternative to the large corporates.</li><li>Initial scale at launch is intended to exceed 100,000m2 with over $50 million in annual turnover</li><li>MFG provides its members with a national network</li></ul></div>
    </div>
    <div class="pillar">
      <div class="pillar-label"><span class="pillar-icon"><svg width="40" height="40" viewBox="0 0 40 40" fill="none" stroke="#39b6ee" stroke-width="3"><path d="M6 22L20 8l14 14M6 34L20 20l14 14"/></svg></span>SYNERGY</div>
      <div class="pillar-body"><ul><li>MFG will provide a centralised business development function on behalf of its members</li><li>Where MFG can leverage its scale, it will provide reduced costs to its members</li></ul></div>
    </div>
    <div class="pillar">
      <div class="pillar-label"><span class="pillar-icon"><svg width="40" height="40" viewBox="0 0 40 40" fill="none" stroke="#39b6ee" stroke-width="3"><path d="M20 4a11 11 0 0 0-6 20v4h12v-4a11 11 0 0 0-6-20zM15 32h10M16 36h8"/></svg></span>VALUE</div>
      <div class="pillar-body"><ul><li>Members' businesses will increase in value as new work is introduced and customer base is diversified</li><li>With its scale, the ultimate sale of MFG will be at higher multiple and value than any individual member could independently achieved</li></ul></div>
    </div>
    <div class="pillar">
      <div class="pillar-label"><span class="pillar-icon"><svg width="40" height="40" viewBox="0 0 40 40" fill="none" stroke="#39b6ee" stroke-width="3"><path d="M14 6h20v28H14M4 20h18M16 14l6 6-6 6"/></svg></span>POTENTIAL<br>EXIT</div>
      <div class="pillar-body"><ul><li>For members who wish to sell some or all of their businesses, MFG will offer to acquire part of their business</li><li>This initial exit will enable owners to "take some cash off the table" and de-risk</li></ul></div>
    </div>
  </div>
</section>

<section class="challenges">
  <h2 class="section-title">THE CHALLENGES</h2>
  <p class="lead">Australian warehouse business owners are facing unprecedented challenges to diversify their client base, compete for work, with national clients, enhance their profitability and ultimately, exit their business.</p>
  <div class="dynamics">
    <h3>AUSTRALIAN WAREHOUSE INDUSTRY DYNAMICS</h3>
    <div class="dyn-grid">
      <div class="dyn-cell">
        <div class="dyn-top"><div role="img" aria-label="Map outline of Australia" style="width:100px;height:84px;background:var(--cyan);border-radius:40% 45% 35% 40%"></div></div>
        <span class="caret">^</span>
        <div class="dyn-bot">Exceptionally fragmented - 1600 businesses across Australia</div>
      </div>
      <div class="dyn-cell">
        <div class="dyn-top">Single site operators - increasing challenge to compete against corporates to secure larger contracts.</div>
        <span class="caret">^</span>
        <div class="dyn-bot"><svg width="96" height="90" viewBox="0 0 96 90" fill="#39b6ee" stroke="#39b6ee" stroke-width="3"><rect x="34" y="32" width="28" height="26" rx="3"/><rect x="6" y="6" width="18" height="16"/><rect x="72" y="6" width="18" height="16"/><rect x="6" y="68" width="18" height="16"/><rect x="72" y="68" width="18" height="16"/><path d="M20 20l16 14M76 20L60 34M20 70l16-14M76 70L60 56" fill="none"/></svg></div>
      </div>
      <div class="dyn-cell">
        <div class="dyn-top"><svg width="90" height="80" viewBox="0 0 90 80"><path d="M10 66a35 35 0 1 1 70 0z" fill="#39b6ee"/><path d="M45 62l18-28" stroke="#1c5ca4" stroke-width="6" stroke-linecap="round"/></svg></div>
        <span class="caret">^</span>
        <div class="dyn-bot">Accelerating industry consolidation</div>
      </div>
      <div class="dyn-cell">
        <div class="dyn-top">Substantial margin pressure - Gross profits falling 3% FY13 to FY15</div>
        <span class="caret">^</span>
        <div class="dyn-bot"><svg width="96" height="86" viewBox="0 0 96 86" fill="#39b6ee"><path d="M4 4v78h88" stroke="#39b6ee" stroke-width="4" fill="none"/><rect x="14" y="40" width="10" height="40"/><rect x="30" y="48" width="10" height="32"/><rect x="46" y="56" width="10" height="24"/><rect x="62" y="64" width="10" height="16"/><path d="M14 14l26 14 14-4 28 26" stroke="#39b6ee" stroke-width="4" fill="none"/><path d="M84 58l-2-14-10 10z"/></svg></div>
      </div>
      <div class="dyn-cell">
        <div class="dyn-top"><svg width="100" height="80" viewBox="0 0 100 80" fill="#39b6ee"><circle cx="22" cy="16" r="10"/><circle cx="50" cy="16" r="10"/><circle cx="78" cy="16" r="10"/><path d="M8 46a14 14 0 0 1 28 0zM36 46a14 14 0 0 1 28 0zM64 46a14 14 0 0 1 28 0z"/><circle cx="36" cy="52" r="8"/><circle cx="64" cy="52" r="8"/><path d="M22 78a14 14 0 0 1 28 0zM50 78a14 14 0 0 1 28 0z"/></svg></div>
        <span class="caret">^</span>
        <div class="dyn-bot">High customer concentration risk</div>
      </div>
      <div class="dyn-cell">
        <div class="dyn-top">Ongoing need to invest in technology to maintain market share</div>
        <span class="caret">^</span>
        <div class="dyn-bot"><svg width="96" height="90" viewBox="0 0 96 90" fill="none" stroke="#39b6ee" stroke-width="5"><circle cx="60" cy="32" r="26"/><circle cx="32" cy="60" r="26" fill="#1c5ca4"/><path d="M40 50h-12a5 5 0 0 0 0 10h8a5 5 0 0 1 0 10H24M32 44v32M68 22h-12a5 5 0 0 0 0 10" stroke-width="4"/></svg></div>
      </div>
    </div>
    <span class="btn-dark">LEARN MORE</span>
  </div>
</section>

<section class="approach">
  <h2 class="section-title">OUR APPROACH</h2>
  <p class="lead">MFG unique approach enable business owners to join with minimal risk, at low cost while retaining control of their business. MFG's approach is focused on achieving maximum value for the business owners over 3 phases:</p>
  <div class="phase-row">
    <span class="phase">National Collective</span>
    <span class="phase">Roll-Up</span>
    <span class="phase">MFG Exit</span>
  </div>
</section>

<section class="membership">
  <h2 class="section-title">KEY MEMBERSHIP TERMS</h2>
  <p class="lead">Meridale Freightworks Group provides a national platform to deliver scale to its members. Through this scale, MFG and its members will secure new business. The value of members' businesses will increase, and members will be presented with multiple options to exit.</p>
  <div class="terms">
    <div class="term">
      <svg viewBox="0 0 80 76" width="80" fill="none" stroke="#39b6ee" stroke-width="6"><path d="M14 20a30 30 0 1 1-4 24"/><path d="M14 6v16h16" /><path d="M50 28H36a6 6 0 0 0 0 12h8a6 6 0 0 1 0 12H30M40 22v36" stroke-width="5"/></svg>
      <h4>Fee Structure</h4>
      <p>MFG membership is primarily success based. Membership includes a low cost annual fee. Success fee paid to MFG based on new work introduced to members.</p>
    </div>
    <div class="term">
      <svg viewBox="0 0 80 76" width="80" stroke="#39b6ee" stroke-width="7" stroke-linecap="round"><path d="M12 10l56 56M30 44L50 30M18 52l12-12M50 30l12-12"/></svg>
      <h4>Alignment</h4>
      <p>Standard level of service must be adopted to secure national accounts. Pricing for new work will be pre-agreed with members.</p>
    </div>
    <div class="term">
      <svg viewBox="0 0 80 76" width="80" fill="none" stroke="#39b6ee" stroke-width="7"><path d="M62 22a30 30 0 1 0 0 32"/><path d="M34 38h40M62 26l12 12-12 12"/></svg>
      <h4>Exit</h4>
      <p>A pre-agreed process for valuing members' businesses will be applied on entry to Phase 2 - on terms demonstrably better than standalone position. Members who retain equity in MFG will cash-out at the same multiple as the MFG founders.</p>
    </div>
    <div class="term">
      <svg viewBox="0 0 80 76" width="80" fill="none" stroke="#39b6ee" stroke-width="5"><circle cx="40" cy="30" r="24"/><path d="M40 16l4 9 10 1-8 6 3 10-9-6-9 6 3-10-8-6 10-1z" fill="#39b6ee" stroke-width="2"/><path d="M26 50l-8 22 10-4 6 8 6-22M54 50l8 22-10-4-6 8-6-22"/></svg>
      <h4>Exclusivity</h4>
      <p>Members will be offered a degree of exclusivity based on geography and service.</p>
    </div>
    <div class="term">
      <svg viewBox="0 0 80 76" width="80" fill="none" stroke="#39b6ee" stroke-width="11" stroke-linecap="round" stroke-linejoin="round"><path d="M10 40l20 20 40-44"/></svg>
      <h4>Complete Flexibility</h4>
      <p>Members have no obligation to progress to Phase 2 (i.e. to sell any of their business)</p>
    </div>
  </div>
</section>

<section class="objectives">
  <h2 class="section-title">OUR OBJECTIVES</h2>
  <p class="lead">MFG intends to deliver tangible benefits to its members resulting in improved profitability, reduced risk and the achievement of measurably higher value. As such MFG offers significant benefits and clear strategic advantages, while presenting a flexible approach with few obligations on members at entry.</p>
  <span class="btn-dark">LEARN MORE</span>
</section>

<section class="team">
  <h2>OUR TEAM</h2>
  <div class="team-bio">
    <p>Daniel Verrick<br>B Eng, MApp Fin, GAICD, FFinsia, CPEng, RPEQ</p>
    <p style="margin-top:12px">M &amp; A Advisory Expertise:</p>
    <ul><li>• $10B in combined transaction experience</li><li>• Tier-1 level M &amp; A and advisory experience</li><li>• Highly discipline approach to business sales</li></ul>
    <ul class="ticks" style="margin-top:16px"><li>25 years' international consulting, advisory experience</li><li>Mergers, acquisitions, and divestment experience</li><li>Large bid management credentials leading bid &gt; $500M</li><li>Responsible manager for Australian Financial Services License</li></ul>
  </div>
  <div class="carousel">
    <svg class="arrow" style="left:-28px" width="20" height="40" viewBox="0 0 20 40" fill="none" stroke="#fff" stroke-width="3"><path d="M16 2L4 20l12 18"/></svg>
    <div class="card side" style="left:0">
      <div class="portrait" role="img" aria-label="Portrait of team member" style="width:88px;height:88px;margin-top:22px"></div>
      <div class="card-name">Owen Hartley</div>
    </div>
    <div class="card main">
      <div class="portrait" role="img" aria-label="Portrait of Daniel Verrick" style="width:112px;height:112px;margin-top:30px"></div>
      <div class="card-name">Daniel Verrick</div>
    </div>
    <div class="card side" style="left:468px">
      <div class="portrait" role="img" aria-label="Portrait of team member" style="width:88px;height:88px;margin-top:22px"></div>
      <div class="card-name">Lena Ashcombe</div>
    </div>
    <svg class="arrow" style="left:648px" width="20" height="40" viewBox="0 0 20 40" fill="none" stroke="#fff" stroke-width="3"><path d="M4 2l12 18L4 38"/></svg>
  </div>
</section>

<section class="contact">
  <div class="contact-info">
    <h2>CONTACT</h2>
    <div class="contact-line"><svg width="18" height="24" viewBox="0 0 18 24" fill="#3a3f47"><path d="M9 0a9 9 0 0 0-9 9c0 7 9 15 9 15s9-8 9-15a9 9 0 0 0-9-9zm0 13a4 4 0 1 1 0-8 4 4 0 0 1 0 8z"/></svg><span>18 Harbourline Drive<br>SYDNEY</span></div>
    <div class="contact-line"><svg width="22" height="18" viewBox="0 0 22 18" fill="#3a3f47"><path d="M1 5c0-3 4-5 10-5s10 2 10 5v2h-5V4H6v3H1zM4 9h14l2 9H2z"/></svg><span>07 3100 4820</span></div>
    <div class="contact-line"><svg width="22" height="16" viewBox="0 0 22 16" fill="#3a3f47"><path d="M0 0h22v16H0z"/><path d="M1 1l10 8 10-8" stroke="#fff" fill="none" stroke-width="1.6"/></svg><span>owen.hartley@merfregro.com.au</span></div>
    <div class="social"><span></span><span></span><span></span></div>
  </div>
  <div class="reach">
    <h2>REACH US NOW</h2>
    <div class="form">
      <div class="field">Name</div>
      <div class="field tall">Message</div>
      <div class="field">Email</div>
      <div class="field">Phone</div>
      <div class="send">SEND</div>
    </div>
  </div>
</section>

<footer class="site-footer">
  <div class="brand">
    <span class="brand-mark"></span>
    <span class="brand-name">MFG</span>
    <span class="brand-sub">MERIDALE FREIGHTWORKS GROUP</span>
  </div>
  <div class="copyright">COPYRIGHT © 2015 MERIDALE FREIGHTWORKS GROUP. ALL RIGHTS RESERVED.</div>
</footer>

</body>
</html>
```